Business Card Design Project

I have just chosen a logo and would now like this designed onto a business card for my hair salon. I would like it to be classy not to busy and have a wow factor when people look at them
Has to Include on card:
Logo Design
And business details below
Kaycee-rae Whitlow (owner)
0481 726 304
Lmv@brindal.com.au
57 Corella Street Kinross Vale
Logo is now attached please provide designs
Hair

```html
<!DOCTYPE html>
<html lang="en">
<head>
<meta charset="utf-8">
<title>Velvet Crown Salon – Business Card</title>
<link rel="stylesheet" href="https://fonts.googleapis.com/css2?family=Parisienne&display=swap">
<style>
  :root {
    --ink: #000000;
    --hair-dark: #151618;
    --hair-mid: #3c3f44;
    --hair-light: #9ea3aa;
    --brand-pink: #d2306f;
    --star-teal: #2f5e6c;
    --text-white: #ffffff;
    --label-bg: #0b1612;
  }
  * { margin: 0; padding: 0; box-sizing: border-box; }
  html, body {
    width: 1200px;
    height: 900px;
    overflow: hidden;
    background: var(--ink);
  }
  .card {
    position: relative;
    width: 1200px;
    height: 900px;
    overflow: hidden;
  }
  .hair-photo {
    position: absolute;
    inset: 0;
    background:
      radial-gradient(ellipse 320px 380px at 330px 420px, rgba(214,170,150,0.55), transparent 70%),
      linear-gradient(115deg, var(--hair-dark) 0%, var(--hair-light) 18%, var(--hair-mid) 32%, var(--hair-dark) 45%, var(--hair-mid) 60%, var(--hair-light) 78%, var(--hair-dark) 100%);
  }
  .info-panel {
    position: absolute;
    left: 610px;
    top: 0;
    width: 530px;
    height: 900px;
    background: var(--ink);
    font-family: "Parisienne", cursive;
    color: var(--text-white);
  }
  .brand-name {
    position: absolute;
    top: 40px;
    left: 0;
    width: 100%;
    text-align: center;
    font-family: "Parisienne", cursive;
    font-size: 92px;
    line-height: 1.1;
    color: var(--brand-pink);
  }
  .label {
    position: absolute;
    background: var(--label-bg);
    text-align: center;
    white-space: nowrap;
  }
  .owner-name {
    left: 11px;
    top: 250px;
    width: 510px;
    height: 118px;
    font-size: 64px;
    line-height: 118px;
  }
  .owner-role {
    left: 180px;
    top: 365px;
    width: 185px;
    height: 66px;
    font-size: 44px;
    line-height: 60px;
  }
  .star {
    position: absolute;
    left: 815px;
    top: 440px;
    width: 128px;
    height: 122px;
  }
  .phone {
    left: 95px;
    top: 590px;
    width: 340px;
    height: 66px;
    font-size: 50px;
    line-height: 66px;
  }
  .email {
    left: 95px;
    top: 668px;
    width: 345px;
    height: 72px;
    font-size: 46px;
    line-height: 72px;
  }
  .address {
    left: 5px;
    top: 742px;
    width: 520px;
    height: 78px;
    font-size: 44px;
    line-height: 78px;
  }
</style>
</head>
<body>
  <main class="card">
    <div class="hair-photo" role="img" aria-label="Photograph of a woman in profile with long glossy black hair spread across the background"></div>
    <section class="info-panel">
      <h1 class="brand-name">Velvet Crown Salon</h1>
      <p class="label owner-name">Kaycee-rae Whitlow</p>
      <p class="label owner-role">(owner)</p>
      <p class="label phone">0481 726 304</p>
      <p class="label email">Lmv@brindal.com.au</p>
      <p class="label address">57 Corella Street Kinross Vale</p>
    </section>
    <svg class="star" viewBox="0 0 100 95" aria-hidden="true">
      <polygon fill="var(--star-teal)" points="50,0 61.8,36.3 100,36.3 69.1,58.8 80.9,95 50,72.6 19.1,95 30.9,58.8 0,36.3 38.2,36.3"/>
    </svg>
  </main>
</body>
</html>
```